We’re a real estate firm that has landed a big builder in a neighboring state. Our branding needs...

We are a real estate firm who represents various builders along with doing resale here in Oregon. Our firm is growing to represent a big builder in Washington State and we’ll have another 40 brokers on our team. We need rebranding. As in, a new logo ( the house logo we have now looks cartoonish, hate it). We need new cards, something to really stand out. I’ve been thinking of using those NFC cards from ZIB or the ones with the seam color. I likely want two or three designs, a darker (as in a background color of black or grey) , a light one ( again I mean background color) and a credit card style (either plastic w an embossed name/number on front, or metal ). I’m thinking dark background for cc, or silver if it’s metal. That’s my thoughts, but you are the artists, so maybe you have an idea I haven’t considered. Our colors were black and red, but we don’t have to stick to that. Just nothing too busy. Oh, and we are typically representing the local, higher quality builders in our area (just below custom), but not national. Subdivisions are near the Kl Marbury, Dovick, and Fallowby Homes sites. We are super excited, but without a lot of time to change the “look” of our brokerage. So I’ll be deciding and moving forward within 24 hours tops. Our name is Real Estate Summitline Group ( we cant change the name because of timeline and business license) Thank you!

Industry/Entity Type

Real Estate

Contact Information for Business Card

The usual. Name of firm. Name of cardholder. Contact info.

Font styles to use
Serif
Sans Serif

Colors

Designer to choose colors to be used in the design.

Requirements
Must have
• A sleek or simple look. I included photos of cards with stylistic attributes we like. Thank you
Nice to have
• We really like the black backgrounds. With foil or embossed detail. We also like the black on black. Matte black card with raised shiny black detail. But still eye catching.
Should not have
• No ornate or busy looking style. We don’t want anything cluttered.

```html
<!DOCTYPE html>
<html lang="en">
<head>
<meta charset="utf-8">
<title>Real Estate Summitline Group – Business Card</title>
<link rel="stylesheet" href="https://fonts.googleapis.com/css2?family=Open+Sans:wght@400;600;700&family=Questrial&display=swap">
<style>
  :root {
    --backdrop: #7d7d7d;
    --card-light: #efefef;
    --navy: #12306a;
    --navy-deep: #0f2c63;
    --ink: #1d1d1d;
    --rule: #b9b9b9;
    --on-navy: #ffffff;
    --on-navy-soft: #d6dbe6;
  }
  * { box-sizing: border-box; margin: 0; padding: 0; }
  html, body { width: 1200px; height: 1200px; overflow: hidden; }
  body {
    background: var(--backdrop);
    font-family: "Open Sans", Arial, sans-serif;
    position: relative;
  }
  .card {
    position: absolute;
    top: 310px;
    height: 594px;
    box-shadow: 2px 3px 6px rgba(0,0,0,0.35);
    text-align: center;
  }
  .card--front {
    left: 234px;
    width: 364px;
    background: var(--card-light);
    color: var(--ink);
  }
  .card--back {
    left: 627px;
    width: 370px;
    background: linear-gradient(180deg, #173a78 0%, var(--navy-deep) 100%);
    color: var(--on-navy);
  }
  .brand {
    position: absolute;
    left: 0; right: 0;
    font-weight: 700;
    line-height: 1.1;
  }
  .brand__mark {
    display: block;
    width: 30px; height: 30px;
    margin: 0 auto 18px;
    background: var(--navy);
  }
  .card--front .brand { top: 118px; color: var(--navy); font-size: 34px; }
  .card--back .brand { top: 262px; color: var(--on-navy); font-size: 34px; }
  .holder {
    position: absolute;
    top: 338px; left: 0; right: 0;
  }
  .holder__name {
    font-family: "Questrial", "Century Gothic", sans-serif;
    font-weight: 700;
    font-size: 25px;
    color: var(--navy);
    letter-spacing: 0.3px;
    -webkit-text-stroke: 0.6px var(--navy);
  }
  .holder__role { font-size: 17px; margin-top: 1px; }
  .rule {
    position: absolute;
    left: 78px; right: 78px;
    height: 1px;
    background: var(--rule);
  }
  .rule--top { top: 396px; }
  .rule--bottom { top: 507px; }
  .contact {
    position: absolute;
    top: 404px; left: 0; right: 0;
    font-size: 17px;
    line-height: 21.7px;
    list-style: none;
  }
  .contact__label { color: var(--navy); font-weight: 600; }
  .contact__web { color: var(--navy); font-weight: 600; }
  .address {
    position: absolute;
    top: 513px; left: 0; right: 0;
    font-size: 17px;
    line-height: 21.7px;
    font-style: normal;
  }
  .back-web {
    position: absolute;
    top: 528px; left: 0; right: 0;
    font-size: 16px;
    font-weight: 600;
    color: var(--on-navy-soft);
    letter-spacing: 0.3px;
  }
</style>
</head>
<body>
  <section class="card card--front" aria-label="Card front">
    <div class="brand">
      <span class="brand__mark"></span>
      Real Estate<br>Summitline Group
    </div>
    <div class="holder">
      <h1 class="holder__name">Marcus Ellery</h1>
      <p class="holder__role">Managing Director</p>
    </div>
    <div class="rule rule--top"></div>
    <ul class="contact">
      <li><span class="contact__label">P:</span> 044-321 654 987</li>
      <li><span class="contact__label">M:</span> 044-321 654 987</li>
      <li><span class="contact__label">E:</span> hello@summitmail.com</li>
      <li class="contact__web">www.summitlinehomes.com</li>
    </ul>
    <div class="rule rule--bottom"></div>
    <address class="address">12345, Address Goes Here<br>Country Name, 123456.</address>
  </section>

  <section class="card card--back" aria-label="Card back">
    <div class="brand">Real Estate<br>Summitline Group</div>
    <p class="back-web">www.summitlinehomes.com</p>
  </section>
</body>
</html>
```